Business card design needed

see my website

www.aldermoorandpike.com

I am after a new logo and business card needs to fit in with the website. I like the look of typewriter text - would like this on the website as well if I could!

Industry/Entity Type

Business

Contact Information for Business Card

Aldermoor and Pike
Design and Heritage Consultants

Marisa Oakton
Principal

+61 407 963 215
marisa@aldermoorandpike.com

www.aldermoorandpike.com

back of card

Interior Design
Consultancy on Period Home restoration and renovation
Heritage Impact Statements
Conservation Management Plans
Materials Conservation
Historical Research

```html
<!DOCTYPE html>
<html lang="en">
<head>
<meta charset="utf-8">
<title>Aldermoor and Pike – Business Card</title>
<link rel="stylesheet" href="https://fonts.googleapis.com/css2?family=Special+Elite&display=swap">
<style>
  :root {
    --teal: #1f9e9c;
    --ink: #1e1e1e;
    --paper-light: #f6f5f2;
    --paper-mid: #e9e7e2;
    --paper-dark: #dcd9d2;
  }
  html, body {
    margin: 0;
    padding: 0;
    width: 1200px;
    height: 741px;
    overflow: hidden;
    background: #ffffff;
  }
  .card {
    position: relative;
    width: 1200px;
    height: 741px;
    overflow: hidden;
  }
  .card__photo {
    position: absolute;
    inset: 0;
    background:
      radial-gradient(ellipse at 50% 25%, var(--paper-light) 0%, rgba(246,245,242,0) 45%),
      linear-gradient(90deg, var(--paper-mid) 0%, var(--paper-light) 40%, var(--paper-mid) 70%, var(--paper-dark) 100%);
  }
  .brand {
    position: absolute;
    left: 30px;
    top: 350px;
    display: flex;
    align-items: center;
    gap: 16px;
  }
  .brand__mark {
    width: 22px;
    height: 22px;
    flex: none;
    background: var(--teal);
  }
  .brand__name {
    margin: 0;
    font-family: "Special Elite", "Courier New", monospace;
    font-weight: 400;
    font-size: 48px;
    line-height: 1;
    color: var(--ink);
    white-space: nowrap;
  }
  .contact {
    position: absolute;
    right: 56px;
    top: 296px;
    margin: 0;
    padding: 0;
    list-style: none;
    font-family: "Special Elite", "Courier New", monospace;
    font-size: 20px;
    color: var(--ink);
    text-align: right;
  }
  .contact__line {
    height: 45.5px;
    display: flex;
    justify-content: flex-end;
    align-items: center;
    gap: 12px;
    white-space: nowrap;
  }
  .contact__icon {
    width: 30px;
    height: 30px;
    flex: none;
  }
</style>
</head>
<body>
<main class="card">
  <div class="card__photo" role="img" aria-label="Faded photograph of a period hallway interior with a pendant lamp, panelled doors, a staircase and a modern white chair"></div>

  <section class="brand">
    <span class="brand__mark" aria-hidden="true"></span>
    <h1 class="brand__name">Aldermoor and Pike</h1>
  </section>

  <ul class="contact">
    <li class="contact__line">Aldermoor and Pike Design and Heritage</li>
    <li class="contact__line">Consultants Marisa Oakton Principal</li>
    <li class="contact__line">
      <span>+61 407 963 215</span>
      <svg class="contact__icon" viewBox="0 0 30 30" aria-hidden="true">
        <path d="M4 12c0-4 5-6 11-6s11 2 11 6v2h-6v-3c-2-1-8-1-10 0v3H4z" fill="var(--teal)"/>
        <path d="M9 14h12l4 10H5z" fill="var(--teal)"/>
        <circle cx="15" cy="19" r="3" fill="#ffffff"/>
      </svg>
    </li>
    <li class="contact__line">
      <span>marisa@aldermoorandpike.com</span>
      <svg class="contact__icon" viewBox="0 0 30 30" aria-hidden="true">
        <rect x="3" y="7" width="24" height="16" fill="var(--teal)"/>
        <path d="M3 7l12 9 12-9" fill="none" stroke="#ffffff" stroke-width="1.8"/>
      </svg>
    </li>
    <li class="contact__line">
      <span>www.aldermoorandpike.com</span>
      <svg class="contact__icon" viewBox="0 0 30 30" aria-hidden="true">
        <circle cx="15" cy="15" r="12" fill="none" stroke="var(--teal)" stroke-width="2.4"/>
        <circle cx="15" cy="15" r="9" fill="var(--teal)"/>
        <path d="M10 10c2-1 4 0 4 2s-3 2-3 4 2 3 1 5c-2 0-4-3-4-6 0-2 1-4 2-5zM17 8c2 0 4 2 5 4-1 1-3 0-4 1s0 3-1 4c-1-1-2-3-1-5s0-3 1-4z" fill="#ffffff"/>
      </svg>
    </li>
  </ul>
</main>
</body>
</html>
```